Domestic Building Company requires professional webpage

We have an existing webpage that was never completed. We are a growing building company specialising in domestic building, renovations and commercial maintenance. We liaise closely with each of our clients to provide quality service they would be happy to recommend. Our easy approachable staff give our clients the confidence to discuss their needs and changes they may have along the way.
Our main source of new customers have been from recommendations of existing clients.
We would like our webpage to reflect our eye for detail and showcase our previous work.
The colour theme should be the same as the colours of our logo.
We would like the main page to really stand out with a slideshow of our pictures of works we have completed.
We would like the tabs to remain the same - Home, About Us, Our Services, Contact us.
In the Our Services section we would like each sub heading to be a link where viewers can see pictures from previous work we have completed.
Our current web page is www.kestrelbuilding.com.au

```html
<!DOCTYPE html>
<html lang="en">
<head>
<meta charset="utf-8">
<title>Kestrel Building Services</title>
<link rel="stylesheet" href="https://fonts.googleapis.com/css2?family=Exo+2:wght@400;500&family=Quicksand:wght@400;500;700&family=Arimo:wght@400;700&display=swap">
<style>
:root{
  --blue:#0a64b4;
  --blue-dark:#0057a8;
  --green:#8cc63f;
  --grey-tab:#58595b;
  --panel:#f1f1f2;
  --panel-edge:#d5d5d7;
  --footer:#5b5b5d;
  --footer-text:#c9c9cb;
  --text:#333;
}
*{box-sizing:border-box;margin:0;padding:0}
html,body{width:1200px;height:891px;overflow:hidden}
body{position:relative;background:#fff;font-family:'Quicksand',sans-serif;color:var(--text)}
.top-bar{position:absolute;left:0;top:0;width:1200px;height:7px;background:var(--blue)}
.header{position:absolute;left:0;top:7px;width:1200px;height:89px;background:linear-gradient(#fbfbfb,#f0f0f1)}
.header-rule{position:absolute;left:0;top:96px;width:1200px;height:3px;background:var(--green)}
.contact-tab{position:absolute;left:646px;top:0;width:412px;height:29px;background:var(--blue);border-radius:0 0 8px 8px;color:#fff;display:flex;align-items:center;gap:34px;padding-left:24px}
.contact-tab .item{display:flex;align-items:center;gap:7px}
.contact-tab .phone{font-family:'Arimo',sans-serif;font-weight:700;font-size:17px}
.contact-tab .email{font-family:'Arimo',sans-serif;font-size:14px}
.brand{position:absolute;left:128px;top:30px;display:flex;align-items:center;gap:10px}
.brand-mark{width:26px;height:26px;background:var(--green)}
.brand-name{font-family:'Quicksand',sans-serif;font-weight:500;font-size:32px;color:var(--blue);line-height:1}
.nav{position:absolute;top:68px;left:604px;display:flex;gap:56px;font-family:'Exo 2',sans-serif;font-size:19px}
.nav a{color:var(--blue);text-decoration:none}
.hero{position:absolute;left:0;top:99px;width:1200px;height:535px;background:linear-gradient(160deg,#6f6459 0%,#8a7b6c 30%,#a69684 55%,#7d7264 80%,#5d544b 100%)}
.panels{position:absolute;left:0;top:634px;width:1200px;height:181px;background:linear-gradient(#e6e6e8,#f4f4f5)}
.panel{position:absolute;top:597px;height:218px;background:var(--panel);border-left:1px solid var(--panel-edge);border-right:1px solid var(--panel-edge)}
.panel-tab{position:absolute;left:0;top:0;height:37px;display:flex;align-items:center}
.panel-tab .flag{width:15px;height:37px}
.panel-tab h2{font-family:'Exo 2',sans-serif;font-weight:400;font-size:23px;color:var(--blue);padding-left:14px}
.panel-tab svg{position:absolute;top:0}
.welcome{left:128px;width:235px}
.services{left:364px;width:471px}
.member{left:835px;width:235px}
.welcome p{position:absolute;left:26px;top:53px;width:200px;font-size:11.3px;line-height:15.7px;color:#333}
.btn{position:absolute;left:50px;top:171px;width:144px;height:30px;background:var(--blue-dark);border:2px solid #8db3d9;color:#fff;font-family:'Arimo',sans-serif;font-weight:700;font-size:12px;display:flex;align-items:center;justify-content:center}
.service-list{position:absolute;list-style:none;top:53px}
.service-list li{display:flex;gap:5px;margin-bottom:15px;font-family:'Arimo',sans-serif;font-size:12.8px;color:var(--blue);line-height:15.7px;text-transform:uppercase}
.service-list li svg{flex:none;margin-top:1px}
.col-a{left:22px;width:230px}
.col-b{left:272px;width:190px}
.badge{position:absolute;left:25px;top:82px;width:185px;height:93px;background:#fff;border:1px solid var(--blue)}
.badge span{position:absolute;left:8px;top:8px;width:64px;height:77px;border-radius:50%;background:#e3ecf6;border:3px solid var(--blue)}
.footer{position:absolute;left:0;top:815px;width:1200px;height:76px;background:var(--footer)}
.legal{position:absolute;left:134px;top:24px;font-size:11.5px;line-height:15px;color:var(--footer-text)}
.social{position:absolute;left:952px;top:24px;display:flex;gap:10px}
.social span{width:34px;height:34px;border-radius:50%;border:2px solid #9aa3ad;background:#6b7078}
</style>
</head>
<body>
<div class="top-bar"></div>
<header class="header"></header>
<div class="header-rule"></div>

<div class="contact-tab">
  <div class="item phone">
    <svg width="12" height="18" viewBox="0 0 12 18"><rect x="0" y="0" width="12" height="18" rx="2" fill="#8cc63f"/><rect x="2" y="2" width="8" height="11" fill="#fff"/><circle cx="6" cy="15.5" r="1.2" fill="#fff"/></svg>
    0400 123 456
  </div>
  <div class="item email">
    <svg width="20" height="14" viewBox="0 0 20 14"><rect width="20" height="14" fill="#8cc63f"/><path d="M0 0 L10 8 L20 0" stroke="#fff" stroke-width="1.5" fill="none"/></svg>
    info@kestrelbuilding.com.au
  </div>
</div>

<div class="brand">
  <span class="brand-mark"></span>
  <span class="brand-name">Kestrel Building Services</span>
</div>

<nav class="nav">
  <a href="#">Home</a>
  <a href="#">About Us</a>
  <a href="#">Our Services</a>
  <a href="#">Contact Us</a>
</nav>

<div class="hero" role="img" aria-label="Slideshow photo of a completed living room renovation with timber floors, sofa and coffee table"></div>
<div class="panels"></div>

<section class="panel welcome">
  <div class="panel-tab">
    <span class="flag" style="background:var(--blue)"></span>
    <h2>Welcome</h2>
  </div>
  <p>Kestrel Building Services Pty Ltd is a construction and renovation company that is based in the Illawarra area. We specialise in all areas of residential and commercial building works and aim to deliver</p>
  <a class="btn">Learn more</a>
</section>

<section class="panel services">
  <div class="panel-tab">
    <span class="flag" style="background:var(--green)"></span>
    <h2>Our Services</h2>
  </div>
  <ul class="service-list col-a">
    <li><svg width="16" height="14" viewBox="0 0 16 14"><circle cx="7" cy="7" r="6" fill="none" stroke="#0a64b4" stroke-width="1.3"/><path d="M3 7 L6.5 11 L15 1" stroke="#f0a30a" stroke-width="2" fill="none"/></svg>Residential house extensions and renovations</li>
    <li><svg width="16" height="14" viewBox="0 0 16 14"><circle cx="7" cy="7" r="6" fill="none" stroke="#0a64b4" stroke-width="1.3"/><path d="M3 7 L6.5 11 L15 1" stroke="#f0a30a" stroke-width="2" fill="none"/></svg>Pergolas</li>
    <li><svg width="16" height="14" viewBox="0 0 16 14"><circle cx="7" cy="7" r="6" fill="none" stroke="#0a64b4" stroke-width="1.3"/><path d="M3 7 L6.5 11 L15 1" stroke="#f0a30a" stroke-width="2" fill="none"/></svg>Decks</li>
    <li><svg width="16" height="14" viewBox="0 0 16 14"><circle cx="7" cy="7" r="6" fill="none" stroke="#0a64b4" stroke-width="1.3"/><path d="M3 7 L6.5 11 L15 1" stroke="#f0a30a" stroke-width="2" fill="none"/></svg>Bathrooms</li>
  </ul>
  <ul class="service-list col-b">
    <li><svg width="16" height="14" viewBox="0 0 16 14"><circle cx="7" cy="7" r="6" fill="none" stroke="#0a64b4" stroke-width="1.3"/><path d="M3 7 L6.5 11 L15 1" stroke="#f0a30a" stroke-width="2" fill="none"/></svg>Commercial fit-out</li>
    <li><svg width="16" height="14" viewBox="0 0 16 14"><circle cx="7" cy="7" r="6" fill="none" stroke="#0a64b4" stroke-width="1.3"/><path d="M3 7 L6.5 11 L15 1" stroke="#f0a30a" stroke-width="2" fill="none"/></svg>Timber flooring</li>
    <li><svg width="16" height="14" viewBox="0 0 16 14"><circle cx="7" cy="7" r="6" fill="none" stroke="#0a64b4" stroke-width="1.3"/><path d="M3 7 L6.5 11 L15 1" stroke="#f0a30a" stroke-width="2" fill="none"/></svg>Aluminium / timber</li>
    <li><svg width="16" height="14" viewBox="0 0 16 14"><circle cx="7" cy="7" r="6" fill="none" stroke="#0a64b4" stroke-width="1.3"/><path d="M3 7 L6.5 11 L15 1" stroke="#f0a30a" stroke-width="2" fill="none"/></svg>Building maintenance</li>
  </ul>
</section>

<section class="panel member">
  <div class="panel-tab">
    <span class="flag" style="background:var(--grey-tab)"></span>
    <h2>Member</h2>
  </div>
  <div class="badge" role="img" aria-label="Industry association membership badge"><span></span></div>
</section>

<footer class="footer">
  <p class="legal">Copyright 2014 Kestrel Building Services Pty Ltd |<br>ABN: 12 345 678 901 | Lic: 123456C</p>
  <div class="social"><span></span><span></span><span></span></div>
</footer>
</body>
</html>
```